SEO marketing site

I need a design only for an SEO/Marketing project I have in mind. I have bought the domain Brivvora.example and want to aim this project at businesses who want to push their business further. WHEN I SAY DESIGN ONLY, I MEAN NO PROGRAMMING. HOWEVER, I DO NEED THE DESIGNER TO PUT THIS SITE ONLINE. $300 IS A LOT OF MONEY FOR A TEMPLATE YOU CAN PURCHASE FOR $60 WITH SOME CUSTOMISATION.

The idea is that businesses will register with us and will be offered two different kinds of services. They can make use of our scripts to check their back links, rankings, compare with competitors and a number of other marketing tools. The other service we provide is that we offer them an SEO service at a very competitive price. We will handle social networking, link building, article submission, directory submission, social bookmarking etc etc at a reasonable monthly fee.

I qoros tram look/flat design is what I really like, and I want to give off a professional vibe. This is the kind of site I wish to go for.

JUST TO REPEAT, I NEED A DESIGN TO BE PUT ONLINE, I.E PSD TO HTML CONVERSION. MY PROGRAMMERS WILL CODE THE CLIENT AREA THEMSELVES.

Target Market(s)

Other businesses

Industry/Entity Type

Marketing

Requirements
Must have
• Qoros 8 or flat design look. Even a site, similar to makerhive, is quite attractive. I would like a killer design for the site.

```html
<!DOCTYPE html>
<html lang="en">
<head>
<meta charset="utf-8">
<title>Brivvora.example – SEO &amp; SEM Services</title>
<link rel="stylesheet" href="https://fonts.googleapis.com/css2?family=Raleway:wght@300;400;600&family=Open+Sans:wght@400;600;700&display=swap">
<style>
:root{
  --dark:#2b2b2b;
  --darker:#222;
  --green:#8cc63f;
  --green-deep:#6aa82a;
  --blue:#3d9ad6;
  --text:#444;
  --muted:#777;
  --light:#f4f4f4;
  --grey:#ececec;
  --white:#fff;
}
*{box-sizing:border-box;margin:0;padding:0}
html,body{width:1200px;height:2444px;overflow:hidden}
body{font-family:"Open Sans",Arial,sans-serif;color:var(--text);background:var(--white);position:relative}
.abs{position:absolute}
/* header */
.site-header{position:absolute;left:0;top:0;width:1200px;height:88px;background:var(--dark)}
.brand{position:absolute;left:183px;top:26px;display:flex;align-items:center;gap:12px;color:var(--green);font-family:"Raleway",sans-serif;font-size:28px;font-weight:400}
.brand-dot{width:32px;height:32px;border-radius:50%;background:var(--green)}
.main-nav{position:absolute;top:18px;left:0;width:1200px;height:60px}
.nav-item{position:absolute;top:0;width:70px;margin-left:-35px;text-align:center;color:var(--white);font-size:14px}
.nav-item svg{display:block;margin:0 auto 4px}
/* hero */
.hero{position:absolute;left:0;top:88px;width:1200px;height:450px;background:linear-gradient(180deg,#f5f8fb 0%,#dfe9f1 45%,#b9cee0 100%);overflow:hidden}
.hero-art{position:absolute;left:0;top:180px;width:1200px;height:270px;background:linear-gradient(180deg,rgba(120,160,200,.15),rgba(70,120,175,.55))}
.hero-figure{position:absolute;left:520px;top:100px;width:430px;height:250px;background:radial-gradient(ellipse at center,rgba(60,90,140,.45),rgba(60,90,140,0) 70%)}
.hero-title{position:absolute;left:196px;top:22px;font-family:"Raleway",sans-serif;font-weight:300;color:#333;font-size:30px;letter-spacing:1px;line-height:1.15;white-space:nowrap}
.hero-title .big{font-size:42px}
.hero-title .sub{font-size:30px}
.account-links{position:absolute;left:862px;top:22px;display:flex;gap:4px}
.account-links span{background:var(--dark);color:var(--white);font-size:13px;padding:7px 11px}
.testimonial{position:absolute;left:200px;top:137px;width:218px;height:252px;background:rgba(40,40,40,.88);color:#eee;padding:20px 14px 12px 28px;font-size:11.5px;line-height:1.38}
.testimonial .quote{position:absolute;left:8px;top:4px;font-size:46px;font-family:"Raleway",sans-serif;color:var(--white)}
.testimonial .author{margin-top:8px;text-align:right;font-size:10px;color:var(--green);line-height:1.3}
.testimonial .more{margin-top:8px;font-size:10px;font-weight:700;text-align:right;color:var(--white)}
.tag{position:absolute;background:rgba(40,60,90,.85);color:var(--white);font-size:11px;padding:3px 8px}
/* contact band */
.contact-band{position:absolute;left:0;top:538px;width:1200px;height:80px;background:var(--green);color:var(--white)}
.contact-band h2{position:absolute;left:220px;top:10px;font-family:"Raleway",sans-serif;font-weight:600;font-size:27px}
.contact-band p{position:absolute;left:220px;top:48px;font-size:17px}
.signup-box{position:absolute;left:806px;top:5px;width:196px;height:70px;background:var(--darker);text-align:center;padding-top:8px}
.signup-box strong{display:block;font-family:"Raleway",sans-serif;font-weight:400;font-size:30px}
.signup-box small{font-size:11px;letter-spacing:3px}
/* newsletter */
.newsletter{position:absolute;left:0;top:618px;width:1200px;height:74px;background:var(--white);border-bottom:1px solid #e4e4e4}
.newsletter p{position:absolute;left:220px;top:27px;font-size:14px}
.newsletter .field{position:absolute;left:626px;top:20px;width:244px;height:36px;border:2px solid var(--green);padding:6px 10px;font-size:14px;color:#333;background:var(--white)}
.newsletter .btn{position:absolute;left:870px;top:20px;width:96px;height:36px;background:var(--green);color:var(--white);font-size:12px;font-weight:700;text-align:center;line-height:36px}
/* service sections */
.service{position:absolute;left:0;width:1200px}
.seo{top:692px;height:506px;background:var(--light)}
.sem{top:1198px;height:513px;background:var(--white)}
.service-title{position:absolute;font-family:"Raleway",sans-serif;font-weight:400;font-size:36px;color:#333}
.service-title .accent{color:var(--green-deep)}
.service-tag{position:absolute;font-family:"Raleway",sans-serif;font-style:italic;font-size:14px;color:#999}
.service-copy{position:absolute;font-size:12.5px;line-height:1.45;color:#555}
.seo .service-copy{width:380px}
.sem .service-copy{width:410px}
.diff-title{position:absolute;font-family:"Raleway",sans-serif;font-weight:400;font-size:26px;color:var(--green-deep)}
.steps{position:absolute;list-style:none}
.steps li{display:flex;align-items:center;gap:12px;height:37px;font-size:13px;color:#444}
.steps b{width:24px;height:24px;border-radius:50%;background:var(--blue);color:var(--white);font-size:12px;display:flex;align-items:center;justify-content:center}
.btn-row{position:absolute;display:flex;gap:22px}
.btn-row span{width:142px;height:34px;line-height:34px;text-align:center;color:var(--white);font-size:13px}
.btn-green{background:var(--green)}
.btn-blue{background:var(--blue)}
.monitor-art{position:absolute;left:600px;top:36px;width:414px;height:360px;background:linear-gradient(135deg,#d7e84a 0%,#8cc63f 45%,#5b9a2c 100%);border:16px solid #1f1f1f;border-bottom-width:60px;border-radius:6px}
.monitor-stand{position:absolute;left:757px;top:396px;width:100px;height:50px;background:linear-gradient(180deg,#d9d9d9,#bdbdbd)}
/* diagram */
.feature-card{position:absolute;width:190px;text-align:center;font-size:11px;color:#555;line-height:1.35}
.feature-card h4{font-size:12px;color:#222;margin:6px 0 4px}
.feature-icon{width:66px;height:66px;margin:0 auto;display:block}
/* coverage */
.coverage{position:absolute;left:0;top:1711px;width:1200px;height:403px;background:var(--grey)}
.coverage h2{position:absolute;top:40px;width:1200px;text-align:center;font-family:"Raleway",sans-serif;font-weight:400;font-size:36px;color:var(--green-deep)}
.cover-item{position:absolute;top:105px;width:140px;margin-left:-70px;text-align:center;font-size:14px;color:#444}
.cover-item svg{display:block;margin:0 auto 18px}
.signup-free{position:absolute;left:500px;top:274px;width:204px;height:48px;background:var(--blue);color:var(--white);font-size:18px;text-align:center;line-height:48px}
/* footer */
.site-footer{position:absolute;left:0;top:2114px;width:1200px;height:252px;background:var(--white)}
.foot-col{position:absolute;top:48px;font-size:11px;color:#666;line-height:2}
.foot-col h5{font-size:15px;font-weight:400;color:#333;margin-bottom:10px}
.about-col{width:340px;line-height:1.5}
.social{display:flex;gap:8px}
.social i{width:22px;height:22px;background:var(--green);border-radius:3px;display:block}
.bottom-bar{position:absolute;left:0;top:2366px;width:1200px;height:78px;background:var(--dark)}
.bottom-bar .brand{top:22px;font-size:24px}
.bottom-bar .brand-dot{width:26px;height:26px}
.copyright{position:absolute;left:465px;top:32px;color:#ccc;font-size:11px}
</style>
</head>
<body>

<header class="site-header">
  <div class="brand"><span class="brand-dot"></span>Brivvora.example</div>
  <nav class="main-nav">
    <div class="nav-item" style="left:599px"><svg width="22" height="20"><path d="M11 1 1 10h3v9h5v-6h4v6h5v-9h3z" fill="#fff"/></svg>Home</div>
    <div class="nav-item" style="left:677px"><svg width="22" height="20"><rect x="2" y="5" width="18" height="13" fill="#fff"/><rect x="7" y="2" width="8" height="4" fill="none" stroke="#fff" stroke-width="2"/></svg>Features</div>
    <div class="nav-item" style="left:782px;width:110px;margin-left:-55px"><svg width="22" height="20"><path d="M2 10 10 2h9v9l-8 8z" fill="#fff"/><circle cx="15" cy="6" r="2" fill="#2b2b2b"/></svg>Plans &amp; Pricing</div>
    <div class="nav-item" style="left:873px"><svg width="22" height="20"><rect x="3" y="2" width="16" height="16" fill="#fff"/><path d="M6 7h10M6 11h10M6 15h6" stroke="#2b2b2b" stroke-width="1.5"/></svg>Blog</div>
    <div class="nav-item" style="left:934px"><svg width="22" height="20"><circle cx="9" cy="9" r="6" fill="none" stroke="#fff" stroke-width="2.5"/><path d="M13 13l6 6" stroke="#fff" stroke-width="3"/></svg>SEO</div>
    <div class="nav-item" style="left:992px"><svg width="22" height="20"><circle cx="11" cy="10" r="8" fill="none" stroke="#fff" stroke-width="2"/><circle cx="11" cy="10" r="4" fill="none" stroke="#fff" stroke-width="2"/><circle cx="11" cy="10" r="1.5" fill="#fff"/></svg>SEM</div>
  </nav>
</header>

<section class="hero">
  <div class="hero-art" role="img" aria-label="Sketched city skyline in blue tones"></div>
  <div class="hero-figure" role="img" aria-label="Businessman with a backpack leaping over the city"></div>
  <h1 class="hero-title"><span>IMPROVE YOUR </span><span class="big">BRAND VISIBILITY</span><br><span class="sub">USING OUR SERVICES</span></h1>
  <div class="account-links"><span>Signin</span><span>Register</span></div>
  <blockquote class="testimonial">
    <span class="quote">“</span>
    wow! these folks are amazing to work with, when we saw amazing results we mean it!! by using their services our business gets numerous leads. They improved our Searchly ranking and we are listing on the first page!! We always recommend them to everyone and friends.
    <div class="author">Mara Lindqvist<br>Orbel Inc, USA</div>
    <div class="more">MORE TESTIMONIALS</div>
  </blockquote>
  <span class="tag" style="left:20px;top:255px">SBT</span>
  <span class="tag" style="left:125px;top:282px">SEM</span>
  <span class="tag" style="left:655px;top:330px">Social marketing</span>
  <span class="tag" style="left:970px;top:310px">Promotions</span>
</section>

<section class="contact-band">
  <h2>Contact brivvora now!</h2>
  <p>We Are A Search Engine optimization &amp; Marketing Specialists.</p>
  <div class="signup-box"><strong>SignUp</strong><small>CLICK HERE</small></div>
</section>

<section class="newsletter">
  <p>Get brivvora's FREE email newsletter, be the First to know!!</p>
  <div class="field">Your email</div>
  <div class="btn">SUBMIT</div>
</section>

<section class="service seo">
  <span class="service-tag" style="left:360px;top:56px">Search Engine Optimization</span>
  <h2 class="service-title" style="left:176px;top:76px"><span class="accent">SEO</span> Services</h2>
  <p class="service-copy" style="left:176px;top:136px">Getting listed in search engines is not a difficult task but what matters is how your site has been listed in a search engine and how well you are ranked. Your site can get higher rankings in all search engines if you follow ethical seo strategies.</p>
  <h3 class="diff-title" style="left:176px;top:214px">How we are different</h3>
  <ol class="steps" style="left:176px;top:256px">
    <li><b>1</b>Prepare a tailor made SEO &amp; SEM proposal</li>
    <li><b>2</b>Monthly Ranking/ Progress Reports sent to client</li>
    <li><b>3</b>Strict monthly maintenance plans</li>
    <li><b>4</b>24/7 hours client support is provided</li>
  </ol>
  <div class="btn-row" style="left:176px;top:412px"><span class="btn-green">LEARN MORE</span><span class="btn-blue">APPLY NOW</span></div>
  <div class="monitor-art" role="img" aria-label="Desktop monitor showing a growth chart with user and lead milestones"></div>
  <div class="monitor-stand" role="img" aria-label="Monitor stand"></div>
</section>

<section class="service sem">
  <svg class="abs" style="left:170px;top:70px" width="420" height="330" viewBox="0 0 420 330">
    <g fill="none" stroke="#999" stroke-width="1.5" stroke-dasharray="4 4">
      <path d="M80 80 Q150 120 200 150"/><path d="M340 80 Q270 120 220 150"/>
      <path d="M80 250 Q150 200 200 170"/><path d="M340 250 Q270 200 220 170"/>
    </g>
    <circle cx="210" cy="160" r="24" fill="#2b4a7a"/>
    <circle cx="210" cy="160" r="14" fill="#fff"/>
  </svg>
  <div class="feature-card" style="left:182px;top:72px">
    <svg class="feature-icon" viewBox="0 0 66 66"><rect width="66" height="66" fill="#e2452f"/><circle cx="33" cy="36" r="14" fill="#fff"/></svg>
    <h4>Boost Your ROI</h4>Lorem Ipsum is simply dummy text of the printing and typesetting</div>
  <div class="feature-card" style="left:402px;top:72px">
    <svg class="feature-icon" viewBox="0 0 66 66"><rect width="66" height="66" fill="#f5a11c"/><path d="M20 26h26l-13 18z" fill="#fff"/></svg>
    <h4>Delivering Results</h4>Lorem Ipsum is simply dummy text of the printing and typesetting</div>
  <div class="feature-card" style="left:182px;top:260px">
    <svg class="feature-icon" viewBox="0 0 66 66"><rect width="66" height="66" fill="#8cc63f"/><circle cx="33" cy="26" r="12" fill="#fff"/><rect x="30" y="36" width="6" height="16" fill="#fff"/></svg>
    <h4>Acquire new customers</h4>Lorem Ipsum is simply dummy text of the printing and typesetting</div>
  <div class="feature-card" style="left:402px;top:260px">
    <svg class="feature-icon" viewBox="0 0 66 66"><rect width="66" height="66" fill="#3d9ad6"/><rect x="18" y="16" width="30" height="34" fill="#fff"/><path d="M23 26h20M23 33h20M23 40h12" stroke="#3d9ad6" stroke-width="2"/></svg>
    <h4>Competitive Research &amp; Analysis</h4>Lorem Ipsum is simply dummy text of the printing and typesetting</div>

  <span class="service-tag" style="left:835px;top:60px">Search Engine Marketing</span>
  <h2 class="service-title" style="left:623px;top:80px"><span class="accent">SEM</span> Services</h2>
  <p class="service-copy" style="left:623px;top:140px">Getting listed in search engines is not a difficult task but what matters is how your site has been listed in a search engine and how well you are ranked. Your site can get higher rankings in all search engines if you follow ethical seo strategies.</p>
  <h3 class="diff-title" style="left:623px;top:218px">How we are different</h3>
  <ol class="steps" style="left:623px;top:258px">
    <li><b>1</b>Prepare a tailor made SEO &amp; SEM proposal</li>
    <li><b>2</b>Monthly Ranking/ Progress Reports sent to client</li>
    <li><b>3</b>Strict monthly maintenance plans</li>
    <li><b>4</b>24/7 hours client support is provided</li>
  </ol>
  <div class="btn-row" style="left:623px;top:415px"><span class="btn-green">LEARN MORE</span><span class="btn-blue">APPLY NOW</span></div>
</section>

<section class="coverage">
  <h2>See What Our Services Cover</h2>
  <div class="cover-item" style="left:260px"><svg width="80" height="80"><rect width="80" height="80" fill="#d6d6d6"/><path d="M18 28h8l6 22h24l6-16H30" fill="none" stroke="#333" stroke-width="4"/><circle cx="36" cy="58" r="4" fill="#333"/><circle cx="52" cy="58" r="4" fill="#333"/></svg>Social Networking</div>
  <div class="cover-item" style="left:400px"><svg width="80" height="80"><g fill="none" stroke="#3b3b3b" stroke-width="7"><rect x="14" y="34" width="28" height="16" rx="8" transform="rotate(-45 28 42)"/><rect x="38" y="30" width="28" height="16" rx="8" transform="rotate(-45 52 38)"/></g></svg>Link Building</div>
  <div class="cover-item" style="left:546px"><svg width="80" height="80"><rect x="18" y="14" width="40" height="52" fill="none" stroke="#3b3b3b" stroke-width="5"/><path d="M26 30h24M26 40h24M26 50h14" stroke="#8cc63f" stroke-width="4"/></svg>Article Submission</div>
  <div class="cover-item" style="left:686px"><svg width="80" height="80"><path d="M14 34h12l28-14v40L26 46H14z" fill="#3b3b3b"/><path d="M60 30l8-6M60 40h10M60 50l8 6" stroke="#8cc63f" stroke-width="4"/></svg>Promotions</div>
  <div class="cover-item" style="left:824px"><svg width="80" height="80"><rect x="12" y="16" width="56" height="44" fill="none" stroke="#3b3b3b" stroke-width="5"/><rect x="12" y="16" width="56" height="10" fill="#8cc63f"/><path d="M40 36l14 8-6 2 4 8-4 2-4-8-4 4z" fill="#3b3b3b"/></svg>Pay per Click</div>
  <div class="cover-item" style="left:954px"><svg width="80" height="80"><rect x="20" y="12" width="40" height="56" fill="#3b3b3b"/><path d="M46 12v24l6-5 6 5V12z" fill="#8cc63f"/></svg>Social Bookmarking</div>
  <div class="signup-free">SIGNUP FOR FREE ➚</div>
</section>

<footer class="site-footer">
  <div class="foot-col about-col" style="left:176px">
    <h5>Brivvora</h5>
    <p>Its a Sample text :</p>
    <p>The idea is that businesses will register with us and will be offered two different kinds of services. They can make use of our scripts to check their back links, rankings, compare with competitors and a number of other marketing tools. The other service we provide is that we offer them an SEO service at a very competitive price. We will handle social networking, link building.</p>
    <p style="text-align:right;color:var(--green-deep)">LEARN MORE</p>
  </div>
  <div class="foot-col" style="left:579px">
    <h5>Resources</h5>About us<br>Blog<br>FAQ<br>Services<br>Why Choose Brivvora
  </div>
  <div class="foot-col" style="left:733px">
    <h5>Services</h5>Search Engine Optimization<br>Search Engine Marketing<br>Blog Optimization<br>Research &amp; Analytics<br>Social Marketing
  </div>
  <div class="foot-col" style="left:909px">
    <h5>Get Social</h5>
    <div class="social"><i></i><i></i><i></i><i></i></div>
  </div>
</footer>

<div class="bottom-bar">
  <div class="brand" style="left:183px"><span class="brand-dot"></span>Brivvora.example</div>
  <p class="copyright">Copyright © 2013-2050 Brivvora Inc. All Rights Reserved.</p>
</div>

</body>
</html>
```